Tattoo Care Kit

We need a retail box for a tattoo care product. The marketing name for this product is brambletoff.

Brambletoff will contain 2 tubes of product: 1) 4% lidocaine and 2) Vitamin A & D cream. Lidocaine will be used to numb the pain immediately after it is designed and the A & D post creation to protect the skin and ink.

Brambletoff is considered an OTC (Over-the-Counter) product/medication so we are looking for that pharma look. Nonetheless, we want to have a "tattoo" parlor element to it: skull, bones, tattoo, etc.

I have enclosed two graphics of the best sellers out there. The Box will be vertical like the vel9 graphic

We are open to foils, embossing, special varnishes and laminated board stock being used on the graphics. Brambletoff will be a very high end product.

```html
<!DOCTYPE html>
<html lang="en">
<head>
<meta charset="utf-8">
<title>Brambletoff Lidocaine – Box and Tube</title>
<link rel="stylesheet" href="https://fonts.googleapis.com/css2?family=Anton&family=Merriweather:wght@400;900&display=swap">
<style>
  :root {
    --canvas: #ffffff;
    --red: #ea3a38;
    --red-deep: #d8283a;
    --ornament: #5a1418;
    --ornament-soft: #8a1c22;
    --ink: #111111;
    --paper: #ffffff;
    --silver-light: #f2f2f2;
    --silver-dark: #b9b9b9;
  }
  html, body {
    margin: 0;
    padding: 0;
    overflow: hidden;
    background: var(--canvas);
  }
  .canvas {
    position: relative;
    width: 1200px;
    height: 1000px;
    overflow: hidden;
    background: var(--canvas);
  }

  /* ---------- Retail box ---------- */
  .box {
    position: absolute;
    left: 282px;
    top: 174px;
    width: 284px;
    height: 652px;
    overflow: hidden;
    background: radial-gradient(ellipse at 45% 55%, var(--red) 0%, var(--red) 45%, var(--red-deep) 100%);
  }

  /* tattoo ornament areas: clean flat shapes */
  .ornament {
    position: absolute;
    border-radius: 50%;
    background: linear-gradient(90deg, var(--ornament-soft) 0%, var(--ornament) 100%);
  }
  .box .ornament--left  { left: -34px; top: 212px; width: 96px;  height: 146px; }
  .box .ornament--right { left: 208px; top: 30px;  width: 130px; height: 500px; }

  .brand-name {
    position: absolute;
    left: 0;
    top: 0;
    overflow: visible;
  }
  .brand-name text {
    font-family: "Anton", sans-serif;
    fill: var(--ink);
    stroke: var(--paper);
    stroke-width: 1.5px;
    paint-order: stroke fill;
  }

  .claim {
    position: absolute;
    left: 0;
    width: 100%;
    text-align: center;
    font-family: "Merriweather", serif;
  }
  .claim__line {
    margin: 0;
    color: var(--paper);
    font-weight: 400;
    letter-spacing: 0.5px;
  }
  .claim__strong {
    margin: 0;
    color: var(--ink);
    font-weight: 900;
    letter-spacing: 0.5px;
  }
  .box .claim { top: 489px; left: -6px; }
  .box .claim__line  { font-size: 12.5px; line-height: 17px; }
  .box .claim__strong { font-size: 18px; line-height: 24px; margin-top: 1px; }

  .volume-ribbon { position: absolute; }
  .box .volume-ribbon { left: 68px; top: 566px; width: 140px; height: 34px; }

  /* ---------- Tube ---------- */
  .tube {
    position: absolute;
    left: 660px;
    top: 170px;
    width: 260px;
    height: 660px;
  }
  .tube__shape {
    position: absolute;
    left: 0;
    top: 0;
  }
  .tube__print {
    position: absolute;
    left: 0;
    top: 0;
    width: 260px;
    height: 540px;
    clip-path: polygon(6px 27px, 250px 27px, 222px 535px, 37px 535px);
  }
  .tube .ornament--left  { left: -10px; top: 186px; width: 92px;  height: 100px; }
  .tube .ornament--right { left: 178px; top: 110px; width: 110px; height: 320px; }
  .tube .claim { top: 387px; left: 0; }
  .tube .claim__line  { font-size: 12px; line-height: 16px; }
  .tube .claim__strong { font-size: 16px; line-height: 22px; margin-top: 2px; }
  .tube .volume-ribbon { left: 67px; top: 470px; width: 126px; height: 24px; }
</style>
</head>
<body>
<main class="canvas">

  <section class="box" aria-label="Brambletoff retail box front">
    <div class="ornament ornament--left" role="img" aria-label="Black tribal tattoo ornament"></div>
    <div class="ornament ornament--right" role="img" aria-label="Large black tribal tattoo wing ornament"></div>

    <svg class="brand-name" width="284" height="652" viewBox="0 0 284 652" role="heading" aria-level="1" aria-label="BRAMBLETOFF">
      <text transform="translate(173 466) rotate(-90)" font-size="100" textLength="395" lengthAdjust="spacingAndGlyphs">BRAMBLETOFF</text>
    </svg>

    <div class="claim">
      <p class="claim__line">LIDOCAINE</p>
      <p class="claim__line">TO NUMB THE PAIN</p>
      <p class="claim__strong">IMMEDIATELY</p>
    </div>

    <svg class="volume-ribbon" viewBox="0 0 140 34" aria-label="40 ml">
      <path d="M2 15 L14 13 L12 19 L16 25 L4 26 Z" fill="#d4d4d4"/>
      <path d="M136 11 L124 10 L126 16 L122 22 L134 22 Z" fill="#d4d4d4"/>
      <path d="M10 13 Q40 8 70 15 Q100 22 130 12 L130 21 Q100 30 70 23 Q40 16 10 22 Z" fill="#ffffff" stroke="#8a8a8a" stroke-width="0.6"/>
      <circle cx="70" cy="17" r="13" fill="#111111" stroke="#ffffff" stroke-width="1.5"/>
      <text x="70" y="20" text-anchor="middle" font-family="Anton, sans-serif" font-size="9" fill="#ffffff">40ml</text>
    </svg>
  </section>

  <section class="tube" aria-label="Brambletoff lidocaine tube">
    <svg class="tube__shape" width="260" height="660" viewBox="0 0 260 660" aria-hidden="true">
      <defs>
        <linearGradient id="tube-body" x1="0" x2="1" y1="0" y2="0">
          <stop offset="0" stop-color="#d9283a"/>
          <stop offset="0.35" stop-color="#ec3e39"/>
          <stop offset="0.7" stop-color="#e83636"/>
          <stop offset="1" stop-color="#d5263a"/>
        </linearGradient>
        <linearGradient id="tube-metal" x1="0" x2="0" y1="0" y2="1">
          <stop offset="0" stop-color="#f4f4f4"/>
          <stop offset="1" stop-color="#bdbdbd"/>
        </linearGradient>
        <linearGradient id="tube-nozzle" x1="0" x2="1" y1="0" y2="0">
          <stop offset="0" stop-color="#000000"/>
          <stop offset="0.4" stop-color="#3a3a3a"/>
          <stop offset="1" stop-color="#050505"/>
        </linearGradient>
      </defs>
      <rect x="6" y="6" width="244" height="22" rx="3" fill="url(#tube-metal)"/>
      <path d="M6 27 L250 27 Q242 45 240 70 L222 535 L37 535 L22 70 Q14 45 6 27 Z" fill="url(#tube-body)"/>
      <path d="M6 27 Q128 50 250 27 L250 31 Q128 54 6 31 Z" fill="#e6e6e6" opacity="0.8"/>
      <path d="M36 535 L223 535 L224 548 Q130 554 36 548 Z" fill="url(#tube-metal)"/>
      <path d="M94 550 L164 550 L164 648 Q164 656 156 656 L102 656 Q94 656 94 648 Z" fill="url(#tube-nozzle)"/>
    </svg>

    <div class="tube__print">
      <div class="ornament ornament--left" role="img" aria-label="Black tribal tattoo ornament"></div>
      <div class="ornament ornament--right" role="img" aria-label="Large black tribal tattoo wing ornament"></div>

      <svg class="brand-name" width="260" height="540" viewBox="0 0 260 540" role="heading" aria-level="2" aria-label="BRAMBLETOFF">
        <text transform="translate(155 378) rotate(-90)" font-size="74" textLength="310" lengthAdjust="spacingAndGlyphs">BRAMBLETOFF</text>
      </svg>

      <div class="claim">
        <p class="claim__line">LIDOCAINE</p>
        <p class="claim__line">TO NUMB THE PAIN</p>
        <p class="claim__strong">IMMEDIATELY</p>
      </div>

      <svg class="volume-ribbon" viewBox="0 0 140 27" aria-label="40 ml">
        <path d="M2 11 L14 9 L12 14 L16 19 L4 20 Z" fill="#d4d4d4"/>
        <path d="M136 8 L124 7 L126 12 L122 17 L134 17 Z" fill="#d4d4d4"/>
        <path d="M10 10 Q40 5 70 11 Q100 17 130 9 L130 16 Q100 24 70 18 Q40 12 10 17 Z" fill="#ffffff" stroke="#8a8a8a" stroke-width="0.6"/>
        <circle cx="70" cy="13.5" r="11" fill="#111111" stroke="#ffffff" stroke-width="1.5"/>
        <text x="70" y="16.5" text-anchor="middle" font-family="Anton, sans-serif" font-size="8" fill="#ffffff">40ml</text>
      </svg>
    </div>
  </section>

</main>
</body>
</html>
```